Progressive European Honey Business needs minimalistic packaging design

Hello - thank you for your interest in our brief. We are Fizzy Vixens, a London based Honey business, importing only the best honey Europe has to offer. Our values are deeply rooted with in progressive liberal values and we are looking for minimalist packaging, which reflects that.

We are looking for a design, which dimensions fit with our packaging option (Velmor Glass Jar | HEIGHT 90mm | DIAMETER 63mm). We will require a various output files (High Resolution JPEG (CMYK Colors 300 dpi) Source File Ai, PSD, PDF, Printing files (die cut, die folding) and a 3D Mockup of the packaging for use within digital commerce platforms.

We must be able to adjust the free text on the label front and it should include the following:
Brand Name
Honey type
Limited edition No. X / 100 ( X being the number of purchase i.e. 25 / 100)
EU Honey, Single Orgin (Germany)
(c) The net weight (250g)

The back must include room for additional information (again adjustable by us) and the following:
“Unsuitable for children under 12 months”
(b) The appropriate durability declaration

In total, we are looking for
a) A front label
b) A back label
c) A seal (round) including the attached bee and logo included in the Zip file.
Do note that a) & b) can also be combined into one design as long as the symmetry on the jar stays intact.

The final design should communicate modern aesthetics, high quality, that are slightly provocative and pop off the shelves.

Hi folks, sorry for the delay in completing this project, but my business partner had a leak in his house. We planned to finalise our review today, but this will have to wait until it's no longer raining in his livingroom. Our sincere apologies!

• See branding guidelines

• Must follow the branding guideline and fonts provided as attachment

```html
<!DOCTYPE html>
<html lang="en">
<head>
<meta charset="utf-8">
<title>Fizzy Vixens – Front Label</title>
<link rel="stylesheet" href="https://fonts.googleapis.com/css2?family=Titan+One&family=Fraunces:opsz,wght@9..144,800&family=Montserrat:wght@700&display=swap">
<style>
  :root {
    --canvas: #ffffff;
    --purple: #7b3a8e;
    --purple-deep: #662a78;
    --orange: #e5804a;
    --orange-light: #f0a468;
    --amber: #f4a62a;
    --bee-yellow: #f2c21b;
    --white: #ffffff;
  }
  html, body {
    margin: 0;
    padding: 0;
    width: 1200px;
    height: 1200px;
    overflow: hidden;
    background: var(--canvas);
  }
  .canvas {
    position: relative;
    width: 1200px;
    height: 1200px;
  }
  .label {
    position: absolute;
    left: 110px;
    top: 165px;
    width: 980px;
    height: 870px;
  }
  .label-art {
    position: absolute;
    inset: 0;
    width: 100%;
    height: 100%;
  }
  .brand-name {
    position: absolute;
    left: 0;
    right: 0;
    top: 92px;
    margin: 0;
    text-align: center;
    font-family: "Titan One", sans-serif;
    font-weight: 400;
    font-size: 128px;
    line-height: 0.98;
    letter-spacing: 2px;
    color: var(--white);
    text-transform: uppercase;
  }
  .tagline {
    font-family: "Fraunces", serif;
    font-weight: 800;
    font-size: 50px;
    fill: var(--white);
  }
  .info-row {
    position: absolute;
    left: 0;
    right: 0;
    top: 768px;
    display: flex;
    justify-content: center;
    gap: 58px;
    font-family: "Montserrat", sans-serif;
    font-weight: 700;
    font-size: 21px;
    line-height: 0.95;
    letter-spacing: 1.5px;
    color: var(--white);
    text-transform: uppercase;
    text-align: center;
  }
  .info-item { margin: 0; }
</style>
</head>
<body>
<main class="canvas">
  <section class="label">
    <svg class="label-art" viewBox="0 0 980 870" xmlns="http://www.w3.org/2000/svg">
      <defs>
        <linearGradient id="bandPurple" x1="0" y1="0" x2="1" y2="0">
          <stop offset="0" stop-color="#6b2d7e"/>
          <stop offset="0.5" stop-color="var(--purple)"/>
          <stop offset="1" stop-color="#6b2d7e"/>
        </linearGradient>
        <path id="taglineArc" d="M 262 680 A 228 228 0 1 1 718 680"/>
      </defs>

      <rect class="band-purple" x="0" y="0" width="980" height="870" fill="url(#bandPurple)"/>

      <path class="band-amber" d="M0 272 Q490 330 980 272 L980 752 Q490 700 0 752 Z" fill="var(--amber)"/>
      <path class="band-honeycomb" role="img" aria-label="Honeycomb pattern in orange tones"
            d="M0 292 Q490 350 980 292 L980 735 Q490 683 0 735 Z" fill="var(--orange)"/>

      <circle class="bee-badge" role="img" aria-label="Illustration of a crowned cartoon bee"
              cx="490" cy="628" r="146" fill="var(--bee-yellow)"/>

      <text class="tagline">
        <textPath href="#taglineArc" startOffset="50%" text-anchor="middle">The Best Europe Honey</textPath>
      </text>
    </svg>

    <h1 class="brand-name">Fizzy<br>Vixens</h1>

    <div class="info-row">
      <p class="info-item">Honey Type<br>Limited Edition<br>No. 25 / 100</p>
      <p class="info-item">Net<br>Weight<br>250G</p>
      <p class="info-item">EU Honey<br>Single Orgin<br>(Germany)</p>
    </div>
  </section>
</main>
</body>
</html>
```